Solar Advertising Flier to generate Biz

I need a advertisement that generates business to be used in a mailer for marketing purposes.

Im attaching a file that is a an idea of advertisement.
I do not want the "ZVN" specific information on it.
I want the background solar panels.
Same information as the ad.
And I've attached my Logo - I want the color scheme to match this.

Thank you

Target Market(s)

Middle to Upper Class Home Owners

Industry/Entity Type

Solar Energy

Requirements
Must have
• A call to action
• A professional look
Nice to have
• A family
• Great looking solar panels
Should not have
• Cartoons

```html
<!DOCTYPE html>
<html lang="en">
<head>
<meta charset="utf-8">
<title>Go Solar Flier – Brightfield Energy</title>
<link href="https://fonts.googleapis.com/css2?family=Montserrat:wght@400;500;600;700;800;900&display=swap" rel="stylesheet">
<style>
  :root{
    --stage:#d9d9da;
    --paper:#ffffff;
    --blue:#1f6fc4;
    --blue-deep:#1b4fa8;
    --blue-bright:#1a8fd6;
    --green:#8cc63f;
    --ink:#3a3a3a;
    --sky-top:#3f86d3;
    --sky-mid:#a9cdee;
  }
  *{box-sizing:border-box;margin:0;padding:0}
  html,body{width:1200px;height:1200px;overflow:hidden}
  body{background:var(--stage);font-family:"Montserrat",sans-serif;color:var(--ink)}
  .flier{position:absolute;left:190px;top:20px;width:820px;height:1160px;background:var(--paper);overflow:hidden;box-shadow:0 6px 24px rgba(0,0,0,.18)}
  .flier svg.art{position:absolute;left:0;top:0}
  .headline{position:absolute;left:30px;top:170px;width:380px;text-align:center}
  .headline .title{font-size:60px;font-weight:900;color:#fff;letter-spacing:1px;line-height:1;white-space:nowrap;
    text-shadow:3px 3px 0 var(--blue-deep),-3px -3px 0 var(--blue-deep),3px -3px 0 var(--blue-deep),-3px 3px 0 var(--blue-deep),0 3px 0 var(--blue-deep),0 -3px 0 var(--blue-deep)}
  .headline .sub{margin-top:12px;font-size:22px;font-weight:800;color:var(--blue-deep);line-height:1.15}
  .tab{position:absolute;background:var(--blue-bright);color:#fff;font-weight:800;font-size:20px;padding:10px 24px;border-radius:0 16px 16px 0}
  .tab.easy{left:0;top:395px;width:330px}
  .tab.how{left:470px;top:470px;width:350px;border-radius:16px 0 0 16px}
  .benefits{position:absolute;left:34px;top:462px;width:400px;list-style:none;font-size:16px;line-height:1.4;color:var(--ink)}
  .benefits li{position:relative;padding-left:18px;margin-bottom:8px}
  .benefits li::before{content:"";position:absolute;left:2px;top:9px;width:7px;height:7px;border-radius:50%;background:var(--blue-bright)}
  .benefits b{font-weight:800}
  .offer{position:absolute;left:70px;top:665px;width:320px;height:225px;border:2px solid #bbb;border-radius:14px;background:#fff;text-align:center;padding-top:22px}
  .offer .lead{font-size:26px;font-weight:800;color:var(--ink);line-height:1.1}
  .offer .amount{font-size:76px;font-weight:900;color:var(--green);line-height:1.05}
  .offer .tail{font-size:26px;font-weight:800;color:var(--ink)}
  .how-copy{position:absolute;left:490px;top:530px;width:315px;font-size:14.5px;line-height:1.5;color:var(--ink)}
  .how-copy .hl{color:var(--blue-bright);font-weight:700}
  .how-copy .cta{color:var(--blue-bright);font-weight:800}
  .brand{position:absolute;left:540px;top:705px;width:260px;display:flex;align-items:center;gap:12px}
  .brand .dot{width:40px;height:40px;border-radius:50%;background:var(--green);flex:none}
  .brand .name{font-size:22px;font-weight:700;color:var(--blue);line-height:1.05}
  .contact{position:absolute;left:580px;top:775px;width:230px;text-align:center;color:var(--ink)}
  .contact .invite{font-size:13px;font-weight:500;line-height:1.3}
  .contact .phone{font-size:27px;font-weight:800;margin:2px 0}
  .contact .addr{font-size:12.5px;font-weight:600;line-height:1.35}
  .contact .web{font-size:14px;font-weight:600;margin-top:2px}
</style>
</head>
<body>
<main class="flier">
  <svg class="art" width="820" height="1160" viewBox="0 0 820 1160">
    <defs>
      <linearGradient id="sky" x1="0" y1="0" x2="0.4" y2="1">
        <stop offset="0" stop-color="var(--sky-top)"/>
        <stop offset="0.55" stop-color="var(--sky-mid)"/>
        <stop offset="1" stop-color="#ffffff" stop-opacity="0"/>
      </linearGradient>
      <linearGradient id="panels" x1="0" y1="0" x2="1" y2="1">
        <stop offset="0" stop-color="#8fbde9"/>
        <stop offset="0.45" stop-color="#2d4fa6"/>
        <stop offset="1" stop-color="#1b2f7a"/>
      </linearGradient>
      <linearGradient id="roof" x1="0" y1="0" x2="1" y2="1">
        <stop offset="0" stop-color="#4b9be6"/>
        <stop offset="0.5" stop-color="#2a3f86"/>
        <stop offset="1" stop-color="#b8582e"/>
      </linearGradient>
    </defs>
    <rect class="sky" x="0" y="0" width="820" height="470" fill="url(#sky)" role="img" aria-label="Blue sky with soft white clouds"/>
    <circle cx="625" cy="225" r="213" fill="#ffffff"/>
    <circle class="photo-panels" cx="625" cy="225" r="205" fill="url(#panels)" role="img" aria-label="Close-up of rooftop solar panels against a bright sky"/>
    <circle cx="625" cy="225" r="205" fill="none" stroke="var(--green)" stroke-width="7"/>
    <path class="wave" d="M0 935 C150 990 300 1030 420 1040 C600 1050 720 1010 820 960 L820 1160 L0 1160 Z" fill="var(--blue)"/>
    <path d="M0 925 C150 980 300 1018 420 1028 C600 1038 720 998 820 948" fill="none" stroke="var(--green)" stroke-width="7"/>
    <circle cx="500" cy="1010" r="148" fill="#ffffff"/>
    <circle class="photo-roof" cx="500" cy="1010" r="140" fill="url(#roof)" role="img" aria-label="Solar panels on a tiled house roof under a sunny sky"/>
    <circle cx="500" cy="1010" r="140" fill="none" stroke="var(--green)" stroke-width="7"/>
  </svg>

  <header class="headline">
    <h1 class="title">GO SOLAR</h1>
    <p class="sub">GET GRANDFATHERED<br>BEFORE THE NEW<br>DEADLINE</p>
  </header>

  <div class="tab easy">WE MAKE IT EASY</div>
  <ul class="benefits">
    <li><b>$0</b> Down, no upfront cost.</li>
    <li>Save up to <b>90%</b> off your utility bill.</li>
    <li>Protect against inflation &amp; energy costs increases from your Utility Company.</li>
    <li>Provide clean, reliable energy for your family <b>powered by the sun.</b></li>
  </ul>

  <div class="offer">
    <p class="lead">CALL TODAY<br>AND RECEIVE A</p>
    <p class="amount">$500</p>
    <p class="tail">CASH REBATE</p>
  </div>

  <div class="tab how">HOW IT WORKS...</div>
  <p class="how-copy">Your solar system allows you to <span class="hl">generate your own clean power</span> and COSTS LESS than your current utility company. Simply pay by the month. Like you do now... but at a Lower rate and <span class="cta">START SAVING IMMEDIATELY.</span></p>

  <div class="brand">
    <span class="dot"></span>
    <span class="name">BRIGHTFIELD<br>ENERGY</span>
  </div>

  <address class="contact">
    <p class="invite">Call Today for a no obligation consultation</p>
    <p class="phone">000-000-0000</p>
    <p class="addr">4418 W Cactus Bloom Rd B-210<br>Sunvale AZ 85000</p>
    <p class="web">www.yourcompanysite.com</p>
  </address>
</main>
</body>
</html>
```